New website for Pollard Law Firm at www.keepwinning-example.com

We are a professional law firm located in the Nashville, Tennessee USA area. We focus on personal injury law. We are looking for a slick new website that is user friendly for updating with new blogs, videos, etc. The primary colors should be red, black, and white. It should load extremely fast and have a good mobile component. The pages for the design will include a home page, about us, news, contact us, and practice page. The practice page will be copied for all the practice areas including motor vehicle accidents, slip and fall accidents, dog bites, etc. We have included an image which we would like to include in the new site which shows the color scheme The image is called banner-Car Wreck. The new website should NOT have gavels, court houses, law books, scales or the typical images for a law firm.

Target Market(s)

People in Tennessee involved in accidents

Industry/Entity Type

Legal services, law firm

Coding

Coded - Design and coding required

Number of Pages Required

5+ page

Font styles to use
Serif

Colors
EB3D1F
EC4F4E
F09395
F8D3D4
FCEDEE

Requirements
Should not have
• Gavels, columns, scales, law related images

```html
<!DOCTYPE html>
<html lang="en">
<head>
<meta charset="utf-8">
<title>Pollard Law Firm — Home</title>
<link rel="stylesheet" href="https://fonts.googleapis.com/css2?family=Cormorant+Garamond:wght@400;500;600&family=Poppins:wght@300;400;500&display=swap">
<style>
  :root {
    --red: #d4272e;
    --red-soft: #ec4f4e;
    --red-pale: #f09395;
    --black: #0b0b0c;
    --ink: #1f1f22;
    --text: #5c5c60;
    --muted: #9a9a9e;
    --rule: #d8d8da;
    --panel: #f6f6f6;
    --white: #ffffff;
  }
  * { box-sizing: border-box; margin: 0; padding: 0; }
  html, body { width: 762px; height: 1200px; overflow: hidden; background: var(--white); }
  body { font-family: "Poppins", sans-serif; color: var(--text); position: relative; }

  .site-header { position: absolute; left: 0; top: 0; width: 762px; height: 85px; background: var(--white); }
  .social { position: absolute; left: 64px; top: 20px; display: flex; gap: 9px; }
  .social span { width: 8px; height: 8px; border-radius: 50%; background: var(--ink); display: block; }
  .brand { position: absolute; left: 0; width: 762px; top: 14px; text-align: center;
    font-family: "Cormorant Garamond", serif; font-weight: 600; font-size: 19px; letter-spacing: 1px; color: var(--red); }
  .phone { position: absolute; right: 64px; top: 18px; display: flex; align-items: center; gap: 5px; font-size: 8px; color: var(--ink); }
  .main-nav { position: absolute; top: 63px; left: 0; width: 762px; display: flex; justify-content: center; gap: 38px;
    font-size: 7px; letter-spacing: .4px; color: var(--ink); text-transform: uppercase; }
  .main-nav .active { color: var(--red); border-bottom: 1px solid var(--red); padding-bottom: 2px; }

  .hero { position: absolute; left: 0; top: 85px; width: 762px; height: 342px; background: var(--black); overflow: hidden; }
  .hero-photo { position: absolute; left: 300px; top: 0; width: 462px; height: 342px;
    background: radial-gradient(ellipse at 55% 55%, #b3121c 0%, #7a0c12 30%, #2b0a0c 60%, var(--black) 85%); }
  .hero-copy { position: absolute; left: 64px; top: 78px; }
  .hero-title { font-family: "Cormorant Garamond", serif; font-weight: 500; font-size: 27px; line-height: 35px;
    letter-spacing: 2.5px; color: var(--white); }
  .hero-text { margin-top: 16px; font-size: 8px; line-height: 14px; letter-spacing: .8px; color: #d6d6d6; width: 260px; }
  .btn-red { display: inline-block; background: var(--red); color: var(--white); font-size: 6px; letter-spacing: .5px;
    text-transform: uppercase; text-align: center; }
  .hero .btn-red { margin-top: 22px; width: 74px; height: 16px; line-height: 16px; }
  .scroll-cue { position: absolute; left: 356px; top: 288px; text-align: center; font-size: 7px; letter-spacing: .6px; color: #bdbdbd; }
  .scroll-cue svg { display: block; margin: 5px auto 0; }

  .about { position: absolute; left: 0; top: 427px; width: 762px; height: 414px; background: var(--panel); }
  .eyebrow { font-size: 7px; letter-spacing: 1.4px; color: var(--red); position: absolute; left: 64px; }
  .section-title { position: absolute; left: 64px; font-family: "Cormorant Garamond", serif; font-weight: 500;
    letter-spacing: 2.2px; color: var(--ink); }
  .accent-rule { position: absolute; left: 64px; width: 49px; height: 1px; background: var(--red-pale); }
  .col { position: absolute; width: 248px; font-size: 5.6px; line-height: 10px; color: var(--text); }
  .col p + p { margin-top: 9px; }
  .btn-outline { position: absolute; width: 74px; height: 17px; border: 1px solid var(--rule); font-size: 6px;
    line-height: 15px; text-align: center; color: var(--ink); text-transform: uppercase; letter-spacing: .4px; background: var(--white); }

  .video { position: absolute; left: 64px; top: 703px; width: 634px; height: 276px;
    background: linear-gradient(180deg, #1c4f78 0%, #2c8db0 35%, #3bb3bf 55%, #9cc7b5 75%, #6a8a5e 100%); }
  .play { position: absolute; left: 299px; top: 120px; }

  .practice-intro { position: absolute; left: 0; top: 979px; width: 762px; height: 221px; background: var(--white); }
  .practice-card-photo { position: absolute; left: 83px; top: 1214px; width: 328px; height: 40px; background: #b32a2a; }
</style>
</head>
<body>
  <header class="site-header">
    <div class="social" aria-label="Social links"><span></span><span></span><span></span><span></span></div>
    <div class="brand">Pollard Law Firm</div>
    <div class="phone">
      <svg width="7" height="7" viewBox="0 0 24 24"><path d="M6.6 10.8a15 15 0 0 0 6.6 6.6l2.2-2.2c.3-.3.7-.4 1-.2 1.1.4 2.3.6 3.6.6.6 0 1 .4 1 1V20c0 .6-.4 1-1 1A17 17 0 0 1 3 4c0-.6.4-1 1-1h3.5c.6 0 1 .4 1 1 0 1.3.2 2.5.6 3.6.1.3 0 .7-.2 1z" fill="#1f1f22"/></svg>
      (615) 555-0142
    </div>
    <nav class="main-nav">
      <span class="active">Home</span><span>Practices</span><span>Our Team</span><span>News</span><span>Contact</span>
    </nav>
  </header>

  <section class="hero">
    <div class="hero-photo" role="img" aria-label="Close-up of a red car in a collision with shattering glass"></div>
    <div class="hero-copy">
      <h1 class="hero-title">Don’t lose<br>what’s legally yours</h1>
      <p class="hero-text">Lorem ipsum dolor sit amet, consetetur sadipscing elitr, sed diam nonumy.</p>
      <span class="btn-red">Contact us</span>
    </div>
    <div class="scroll-cue">scroll down
      <svg width="10" height="14" viewBox="0 0 10 14"><rect x="1" y="1" width="8" height="12" rx="4" fill="none" stroke="#bdbdbd" stroke-width=".8"/><line x1="5" y1="3.5" x2="5" y2="6" stroke="#bdbdbd" stroke-width=".8"/></svg>
    </div>
  </section>

  <section class="about">
    <span class="eyebrow" style="top:36px">about</span>
    <h2 class="section-title" style="top:52px;font-size:22px">Trial Lawyers...</h2>
    <span class="accent-rule" style="top:104px"></span>
    <div class="col" style="left:129px;top:100px">
      <p>WE ARE TRIAL LAWYERS AND WE ARE PROUD OF IT. There are many law firms in Tennessee who claim to be trial lawyers, but their attorneys have never seen a courtroom. We have tried hundreds of cases to verdict and helped thousands of people across Tennessee. We fight against billion dollar insurance companies and the State of Tennessee, and we win.</p>
      <p>Our motto is “Don’t Lose What is Legally Yours”. We are the only law firm in Tennessee with the website www.keepwinning-example.com. We strive to help our clients do everything we can to make sure they don’t lose their money, their license or their family. We cannot make guarantees, but we can assure every client we will do everything possible to protect what is theirs.</p>
    </div>
    <div class="col" style="left:458px;top:100px">
      <p>It is very hard not to take each case personally. Our clients include victims of personal injury who did not ask for the pain from a car wreck, professionals trying to provide for their family, and parents falsely accused in a child custody proceeding. Most of our clients are referred by other attorneys who need our specialized expertise. Given what is at stake, we take each client’s matter personally and try to work on each case every day in order to bring justice to our clients.</p>
    </div>
    <span class="btn-outline" style="left:458px;top:237px">Our team</span>
  </section>

  <div class="video" role="img" aria-label="Aerial view of a turquoise bay with sailboats on a beach">
    <svg class="play" width="36" height="36" viewBox="0 0 36 36"><circle cx="18" cy="18" r="15" fill="#fff" opacity=".35"/><circle cx="18" cy="18" r="10" fill="#fff"/><path d="M15.5 13.5v9l7-4.5z" fill="#d4272e"/></svg>
  </div>

  <section class="practice-intro">
    <span class="eyebrow" style="top:55px">practice</span>
    <h2 class="section-title" style="top:80px;font-size:25px">Areas of Practice</h2>
    <span class="accent-rule" style="top:150px"></span>
    <div class="col" style="left:129px;top:145px;width:215px"><p>We handle motor vehicle accidents, slip and fall injuries, dog bites and more. Each case gets a lawyer who knows the courtroom, the insurers and the people of Tennessee. Call us today.</p></div>
    <div class="col" style="left:410px;top:145px;width:215px"><p>When an accident changes your life, we step in fast to gather evidence, deal with insurers and push for the full value of your claim.</p></div>
  </section>
  <div class="practice-card-photo" role="img" aria-label="Paramedic caring for an injured woman beside a vehicle"></div>
</body>
</html>
```